Essential Oil 15ml - package of 6

Design of a box of 6 different essential oils.
+ design of the bottle stickers
My bottles are 15ml clear blue glass.

The pictures attached are my competitors...

Target Market(s)

BRELLICK USA

Font styles to use
Serif

Requirements
Must have
• Our logo + "essential oil" and type (lavender, eucalyptus etc....)
• 15ml - 0.50 fl.oz.
• special color for the oil type.

```html
<!DOCTYPE html>
<html lang="en">
<head>
<meta charset="utf-8">
<title>Solen Vale Essential Oil Labels</title>
<link rel="stylesheet" href="https://fonts.googleapis.com/css2?family=Alegreya+Sans:wght@500&family=Playfair+Display:wght@400;500&display=swap">
<style>
  :root {
    --bg: #f2f2f2;
    --label-dark: #2f2f31;
    --meadow: #4a4a4d;
    --brand-ink: #2b2624;
    --white: #f4f1ea;
    --lemon: #f0a930;
    --eucalyptus: #ef343a;
    --lavender: #9a34e0;
  }
  * { box-sizing: border-box; margin: 0; padding: 0; }
  html, body { width: 1200px; height: 900px; overflow: hidden; }
  body {
    background: var(--bg);
    display: flex;
    align-items: center;
    justify-content: center;
    gap: 44px;
  }
  .label {
    width: 330px;
    height: 470px;
    display: flex;
    flex-direction: column;
    box-shadow: 0 6px 18px rgba(0,0,0,0.12);
    overflow: hidden;
  }
  .label--lemon { --accent: var(--lemon); }
  .label--eucalyptus { --accent: var(--eucalyptus); }
  .label--lavender { --accent: var(--lavender); }

  .brand-band {
    height: 170px;
    background: var(--accent);
    display: flex;
    align-items: center;
    justify-content: center;
    gap: 12px;
  }
  .brand-mark {
    width: 22px; height: 22px;
    border-radius: 50%;
    background: var(--brand-ink);
  }
  .brand-name {
    font-family: "Alegreya Sans", sans-serif;
    font-weight: 500;
    font-size: 42px;
    color: var(--brand-ink);
  }

  .oil-panel {
    flex: 1;
    background: var(--label-dark);
    position: relative;
    display: flex;
    flex-direction: column;
    align-items: center;
    padding: 26px 14px 0;
  }
  .crest-arc { width: 150px; height: 18px; }
  .oil-row {
    display: flex;
    align-items: center;
    justify-content: center;
    gap: 6px;
    margin-top: 4px;
    height: 42px;
  }
  .sprig {
    flex: 0 0 42px;
    height: 24px;
    border-radius: 50%;
    background: linear-gradient(90deg, transparent, var(--accent));
    opacity: 0.75;
  }
  .sprig--right { background: linear-gradient(270deg, transparent, var(--accent)); }
  .oil-name {
    font-family: "Playfair Display", serif;
    font-weight: 400;
    font-size: 34px;
    letter-spacing: 5px;
    color: var(--white);
    line-height: 1;
    white-space: nowrap;
  }
  .label--eucalyptus .oil-name { font-size: 23px; letter-spacing: 2px; }
  .label--lavender .oil-name { font-size: 26px; letter-spacing: 3px; }
  .oil-kind {
    font-family: "Playfair Display", serif;
    font-size: 13px;
    letter-spacing: 1.5px;
    color: var(--accent);
    margin-top: 8px;
  }
  .base-arc { width: 170px; height: 20px; margin-top: 2px; }
  .blossom {
    width: 90px; height: 34px;
    margin-top: 2px;
    border-radius: 45%;
    background: radial-gradient(ellipse at center, var(--accent) 0%, transparent 70%);
    opacity: 0.8;
  }
  .meadow {
    position: absolute;
    left: 0; right: 0; bottom: 30px;
    height: 44px;
    background: linear-gradient(180deg, transparent, var(--meadow));
  }
  .volume {
    position: absolute;
    bottom: 10px;
    left: 0; right: 0;
    text-align: center;
    font-family: "Playfair Display", serif;
    font-size: 13px;
    color: var(--white);
  }
</style>
</head>
<body>

  <section class="label label--lemon">
    <header class="brand-band">
      <span class="brand-mark"></span>
      <span class="brand-name">Solen Vale</span>
    </header>
    <div class="oil-panel">
      <svg class="crest-arc" viewBox="0 0 150 18"><path d="M5 16 Q75 -4 145 16" fill="none" stroke="var(--accent)" stroke-width="2"/></svg>
      <div class="oil-row">
        <div class="sprig" role="img" aria-label="Leafy sprig ornament"></div>
        <h2 class="oil-name">LEMON</h2>
        <div class="sprig sprig--right" role="img" aria-label="Leafy sprig ornament"></div>
      </div>
      <p class="oil-kind">100% ESSENTIAL OIL</p>
      <svg class="base-arc" viewBox="0 0 170 20"><path d="M5 2 Q85 26 165 2" fill="none" stroke="var(--accent)" stroke-width="1.5"/></svg>
      <div class="blossom" role="img" aria-label="Flower spray ornament"></div>
      <div class="meadow" role="img" aria-label="Meadow of grass and flowers silhouette"></div>
      <p class="volume">15ml - 0.50 fl.oz.</p>
    </div>
  </section>

  <section class="label label--eucalyptus">
    <header class="brand-band">
      <span class="brand-mark"></span>
      <span class="brand-name">Solen Vale</span>
    </header>
    <div class="oil-panel">
      <svg class="crest-arc" viewBox="0 0 150 18"><path d="M5 16 Q75 -4 145 16" fill="none" stroke="var(--accent)" stroke-width="2"/></svg>
      <div class="oil-row">
        <div class="sprig" role="img" aria-label="Leafy sprig ornament"></div>
        <h2 class="oil-name">EUCALYPTUS</h2>
        <div class="sprig sprig--right" role="img" aria-label="Leafy sprig ornament"></div>
      </div>
      <p class="oil-kind">100% ESSENTIAL OIL</p>
      <svg class="base-arc" viewBox="0 0 170 20"><path d="M5 2 Q85 26 165 2" fill="none" stroke="var(--accent)" stroke-width="1.5"/></svg>
      <div class="blossom" role="img" aria-label="Flower spray ornament"></div>
      <div class="meadow" role="img" aria-label="Meadow of grass and flowers silhouette"></div>
      <p class="volume">15ml - 0.50 fl.oz.</p>
    </div>
  </section>

  <section class="label label--lavender">
    <header class="brand-band">
      <span class="brand-mark"></span>
      <span class="brand-name">Solen Vale</span>
    </header>
    <div class="oil-panel">
      <svg class="crest-arc" viewBox="0 0 150 18"><path d="M5 16 Q75 -4 145 16" fill="none" stroke="var(--accent)" stroke-width="2"/></svg>
      <div class="oil-row">
        <div class="sprig" role="img" aria-label="Leafy sprig ornament"></div>
        <h2 class="oil-name">LAVENDER</h2>
        <div class="sprig sprig--right" role="img" aria-label="Leafy sprig ornament"></div>
      </div>
      <p class="oil-kind">100% ESSENTIAL OIL</p>
      <svg class="base-arc" viewBox="0 0 170 20"><path d="M5 2 Q85 26 165 2" fill="none" stroke="var(--accent)" stroke-width="1.5"/></svg>
      <div class="blossom" role="img" aria-label="Flower spray ornament"></div>
      <div class="meadow" role="img" aria-label="Meadow of grass and flowers silhouette"></div>
      <p class="volume">15ml - 0.50 fl.oz.</p>
    </div>
  </section>

</body>
</html>
```